New Webpage for High Class Expert Witness Services Company

We are looking for a minimalist design for a webpage that just has our logo and an entry form offer to connect with one of our Liaisons.
The entry form should just ask for Name, Email, Contact Info and Description of Project.

Company Name is: The Marlowe Crest Defense Services

Number of Pages Required

1 page

```html
<!DOCTYPE html>
<html lang="en">
<head>
<meta charset="utf-8">
<title>The Marlowe Crest Defense Services — Contact</title>
<link rel="stylesheet" href="https://fonts.googleapis.com/css2?family=Cinzel:wght@400;500&family=Figtree:wght@400;500;700&display=swap">
<style>
  :root {
    --ink: #000000;
    --text: #111111;
    --muted: #555555;
    --placeholder: #6b6b6b;
    --page: #f3f3f3;
    --page-light: #fafafa;
    --card: #ffffff;
    --line: #e6e6e6;
    --white: #ffffff;
  }
  * { box-sizing: border-box; margin: 0; padding: 0; }
  html, body { width: 1200px; height: 810px; overflow: hidden; }
  body {
    position: relative;
    font-family: "Figtree", sans-serif;
    color: var(--text);
    background: var(--page);
  }
  .backdrop {
    position: absolute; inset: 0;
    background:
      radial-gradient(ellipse 420px 360px at 1150px 60px, #e4e4e4 0%, rgba(228,228,228,0) 100%),
      radial-gradient(ellipse 420px 340px at 40px 720px, #e2e2e2 0%, rgba(226,226,226,0) 100%),
      radial-gradient(ellipse 500px 400px at 500px 560px, var(--page-light) 0%, rgba(250,250,250,0) 100%),
      var(--page);
  }
  .brand {
    position: absolute; left: 171px; top: 46px;
    display: flex; align-items: center; gap: 12px;
  }
  .brand-mark { width: 46px; height: 46px; background: var(--ink); }
  .brand-name {
    font-family: "Cinzel", serif; font-weight: 500;
    font-size: 21px; line-height: 23px; letter-spacing: 0.5px;
    color: var(--ink);
  }
  .contact-btn {
    position: absolute; left: 913px; top: 56px;
    width: 112px; height: 40px; border-radius: 20px;
    background: var(--ink); color: var(--white);
    font-weight: 700; font-size: 13px;
    display: flex; align-items: center; justify-content: center;
  }
  .intro { position: absolute; left: 171px; top: 264px; }
  .intro-title {
    font-family: "Cinzel", serif; font-weight: 400;
    font-size: 58px; line-height: 60px; color: var(--ink);
    letter-spacing: 0.5px;
  }
  .intro-copy {
    margin-top: 12px; width: 345px;
    font-size: 13.5px; line-height: 18px; color: var(--muted);
  }
  .form-card {
    position: absolute; left: 637px; top: 161px;
    width: 388px; height: 521px;
    background: var(--card); border: 1px solid var(--line);
    border-radius: 12px; padding: 20px 22px 0 22px;
  }
  .field-label {
    display: block; font-size: 11.5px; font-weight: 500;
    color: var(--ink); line-height: 14px; margin-bottom: 5px;
  }
  .field {
    height: 55px; border: 1px solid var(--line); border-radius: 14px;
    padding: 0 13px; display: flex; align-items: center;
    font-size: 11.5px; color: var(--placeholder); margin-bottom: 18px;
  }
  .field.area { height: 77px; margin-bottom: 14px; }
  .consent { display: flex; gap: 8px; }
  .consent-box {
    flex: none; width: 17px; height: 17px; margin-top: 4px;
    border: 1px solid #cfcfcf; border-radius: 5px;
  }
  .consent-text { font-size: 11.5px; line-height: 18px; color: var(--muted); }
  .consent-text a { color: var(--muted); font-weight: 700; text-decoration: underline; }
  .submit-btn {
    margin-top: 20px; height: 55px; border-radius: 28px;
    background: var(--ink); color: var(--white);
    font-weight: 700; font-size: 13.5px;
    display: flex; align-items: center; justify-content: center;
  }
</style>
</head>
<body>
  <div class="backdrop" role="img" aria-label="Soft grey quilted diamond texture"></div>

  <header class="brand">
    <div class="brand-mark"></div>
    <div class="brand-name">The Marlowe Crest<br>Defense Services</div>
  </header>
  <div class="contact-btn">Contact Us</div>

  <section class="intro">
    <h1 class="intro-title">CONNECT<br>WITH ONE<br>OF OUR<br>LIAISONS</h1>
    <p class="intro-copy">We’d love to hear about your organization’s needs. Tell us about your project and a member of our team will be in touch with you.</p>
  </section>

  <form class="form-card">
    <label class="field-label">Name</label>
    <div class="field">Enter Your Full Name</div>
    <label class="field-label">Email</label>
    <div class="field">your@example.com</div>
    <label class="field-label">Contact No.</label>
    <div class="field">Enter Your Phone Number</div>
    <label class="field-label">How Can We Help?</label>
    <div class="field area">Description of Project.</div>
    <div class="consent">
      <span class="consent-box"></span>
      <p class="consent-text">I agree to receive other communications from The Marlowe Crest Defense. View our <a>Privacy Policy.</a></p>
    </div>
    <div class="submit-btn">Submit and Continue</div>
  </form>
</body>
</html>
```